依頼詳細
現在当社で作成したチラシを元にしてフリーの挿絵や写真を利用して構成をしてください。イラレで作成したチラシデーターがダウンロードできます。
文章に関しては元がありますが言い回しなど変更していただいて結構です。
ロゴなどのデーターはそのまま使用をしてください。
サイズはB4でお願いします。
訪問看護と訪問介護の比率ですが、現在訪問介護が小さくなっていますが一緒にしていただいてかまいません。
記載項目
ロゴはかならず入れてください。訪問介護のロゴも募集しています。
希望イメージ
シンプル 複雑
単色 カラフル
暗い 明るい
日常 高級
遊び心 厳粛
未来的 伝統的
女性的 男性的
希望する色
緑系、黄・オレンジ系
納品ファイル
• 高解像度JPG (.jpg)
• イラストレーター形式 (.ai)
• フォトショップ形式 (.psd)
補足説明
となりに同グループの別会社があります。
内容等がほぼ同じなので当社とは別に採用させていただく可能性があります。
■ 選んだ理由

一番最初にご提案頂いたのですが、衝撃だったのがプロってここまですごいんだなという事でした。構成の仕方から文字の並べ方完璧です。
自分の中ではtoka-tokaさんが基準となっていたのですが、特にこれ良くない?って言ったわけではないですが10人のスタッフが全員toka-tokaさんを選択致しました。(びっくり)

■ 提案者全員のお礼・コメント

今回ご提案頂きましてありがとうございます。
次回の求人広告等で使用したい方もいたので個別にご連絡させて頂きます。
また、同じグループで求人を行っているところがあります。
今回ご提案頂いた案件に関して、JPgを保存しましたので各事業所に見てもらいますのでオファーがあった場合は買い取りさせていただきます。データーは保持してください。
当社でも別な施設オープンの際は改めてご連絡させて頂きます。
ありがとうございました。

```html
<!DOCTYPE html>
<html lang="ja">
<head>
<meta charset="utf-8">
<title>訪問看護師・訪問介護士 募集</title>
<link href="https://fonts.googleapis.com/css2?family=Dela+Gothic+One&family=M+PLUS+Rounded+1c:wght@500;700;800;900&family=Noto+Sans+JP:wght@400;500;700;900&display=swap" rel="stylesheet">
<style>
:root{
  --orange:#f29600;
  --yellow:#f7cf3c;
  --yellow-light:#fff3b0;
  --green:#5bb531;
  --green-deep:#2f8a2a;
  --green-light:#dff0c8;
  --red:#e5171f;
  --ink:#2a2a2a;
  --white:#ffffff;
  --black:#111111;
}
*{margin:0;padding:0;box-sizing:border-box}
html,body{width:846px;height:1200px;overflow:hidden;background:var(--white)}
body{position:relative;font-family:"Noto Sans JP",sans-serif;color:var(--ink)}
.hero{position:absolute;left:0;top:0;width:846px;height:600px;
  background:radial-gradient(ellipse at 50% 35%,var(--yellow-light) 0%,var(--yellow) 70%);overflow:hidden}
.hills{position:absolute;left:0;top:380px;width:846px;height:220px}
.job-tags{position:absolute;left:150px;top:22px;display:flex;gap:26px}
.job-tag{display:flex;gap:3px}
.job-tag span{width:44px;height:46px;background:var(--orange);color:var(--white);
  font:900 32px/46px "M PLUS Rounded 1c",sans-serif;text-align:center;border-radius:4px}
.headline{position:absolute;left:160px;top:72px;font:400 196px/1 "Dela Gothic One",sans-serif;
  color:var(--orange);-webkit-text-stroke:12px var(--white);paint-order:stroke fill;letter-spacing:-6px;white-space:nowrap}
.intro{position:absolute;left:22px;top:292px;width:142px;font-size:11px;line-height:1.75;font-weight:500}
.workplace{position:absolute;left:676px;top:124px;width:160px}
.workplace h3{font:800 15px "M PLUS Rounded 1c",sans-serif;color:var(--ink)}
.workplace p{font-size:9px;line-height:1.5}
.illus-house{position:absolute;left:650px;top:282px;width:182px;height:150px;border-radius:10px;
  background:linear-gradient(160deg,#f7a35a,#e2593b 60%,#f3e2c3)}
.illus-people{position:absolute;left:345px;top:318px;width:220px;height:240px;border-radius:110px 110px 20px 20px;
  background:linear-gradient(180deg,#f6c9a5,#e8a17a 50%,#8a8f99)}
.briefing{position:absolute;left:176px;top:346px;width:160px;text-align:center}
.briefing .ribbon{display:inline-block;background:var(--green);color:var(--white);font-size:10px;font-weight:700;padding:2px 8px;border-radius:10px;transform:rotate(-8deg)}
.briefing h2{font:900 27px/1.15 "M PLUS Rounded 1c",sans-serif;color:var(--red);margin-top:6px}
.briefing p{font-size:10px;line-height:1.5;color:var(--ink);margin-top:6px}
.company-note{position:absolute;left:596px;top:446px;width:236px;font-size:10px;line-height:1.7;color:var(--white);font-weight:500}
.cols{position:absolute;left:0;top:612px;width:846px;display:flex;gap:30px;padding:0 22px}
.col{flex:1;min-width:0}
.col-title{font:900 22px/1.35 "M PLUS Rounded 1c",sans-serif;color:var(--green-deep)}
.col-title .dot{color:var(--orange)}
.pay{margin-top:8px;font-size:13px}
.pay-row{display:flex;align-items:baseline;gap:8px;padding:5px 0;border-bottom:1px dashed #bbb}
.pay-tag{flex:none;background:var(--orange);color:var(--white);font-size:11px;font-weight:700;padding:2px 8px;border-radius:3px}
.pay-tag.part{background:var(--green)}
.pay strong{font:900 21px "M PLUS Rounded 1c",sans-serif;color:var(--red)}
.pay small{font-size:10px}
.helper-grid{display:grid;grid-template-columns:auto 1fr auto 1fr;gap:4px 8px;align-items:baseline;margin-top:6px;font-size:11px}
.helper-grid strong{font:900 19px "M PLUS Rounded 1c",sans-serif;color:var(--red)}
.terms{margin-top:10px;font-size:11px;line-height:1.65}
.terms dt{float:left;clear:left;width:52px;font-weight:700;color:var(--green-deep)}
.terms dd{margin-left:56px}
.org{margin-top:14px;display:flex;align-items:center;gap:8px}
.org-mark{flex:none;width:36px;height:36px;border-radius:50%;background:var(--green)}
.org-name{font:800 16px "M PLUS Rounded 1c",sans-serif;color:var(--green-deep);line-height:1.25}
.org-name small{display:block;font:400 9px "Noto Sans JP",sans-serif;color:var(--ink)}
.contact{position:absolute;left:0;top:1082px;width:846px;height:88px;background:var(--green-light);
  display:flex;align-items:center;padding:0 24px;gap:14px}
.contact .label{font-size:10px;font-weight:700;color:var(--green-deep);writing-mode:vertical-rl}
.contact .phone{font:900 40px "M PLUS Rounded 1c",sans-serif;color:var(--green-deep);display:flex;align-items:center;gap:6px}
.contact .person{font-size:16px;font-weight:700;color:var(--ink)}
.footer-bar{position:absolute;left:0;top:1170px;width:846px;height:30px;background:var(--black);color:var(--white);
  font-size:14px;font-weight:700;text-align:center;line-height:30px}
</style>
</head>
<body>
<section class="hero">
  <svg class="hills" viewBox="0 0 846 220" preserveAspectRatio="none" aria-hidden="true">
    <path d="M0 120 Q200 40 420 110 T846 70 V220 H0Z" fill="#8cc63f"/>
    <path d="M0 160 Q260 90 520 150 T846 110 V220 H0Z" fill="#5bb531"/>
  </svg>
  <div class="job-tags">
    <div class="job-tag"><span>訪</span><span>問</span><span>看</span><span>護</span><span>師</span></div>
    <div class="job-tag"><span>訪</span><span>問</span><span>介</span><span>護</span><span>士</span></div>
  </div>
  <h1 class="headline">募集!</h1>
  <p class="intro">スタッフを大事にする職場です。ブランクのある方も経験豊富な先輩が丁寧にサポートします。家庭と両立しながら、地域の方の暮らしを一緒に支えていきませんか。まずはお気軽にご相談ください。</p>
  <div class="workplace">
    <h3>勤務地</h3>
    <p>緑ヶ丘市中央区本町1-2-3<br>(本町駅より徒歩5分)</p>
  </div>
  <div class="illus-house" role="img" aria-label="赤い屋根の家と木のイラスト"></div>
  <div class="illus-people" role="img" aria-label="車椅子の高齢者に寄り添う看護師のイラスト"></div>
  <div class="briefing">
    <span class="ribbon">見学・体験 大歓迎!</span>
    <h2>事前説明会<br>随時開催!</h2>
    <p>「話だけでも聞いてみたい」<br>という方もどうぞ</p>
  </div>
  <p class="company-note">当社は在宅で療養される方とご家族を支える訪問看護ステーションです。看護師やリハビリ職が連携し、住み慣れた地域での生活をお手伝いしています。</p>
</section>

<main class="cols">
  <section class="col">
    <h2 class="col-title"><span class="dot">●</span>正看護師 <span class="dot">●</span>PT・ST・OT</h2>
    <div class="pay">
      <div class="pay-row"><span class="pay-tag">正社員</span>月給 <strong>28万円〜</strong></div>
      <div class="pay-row"><span class="pay-tag">正社員</span>訪問単価 <strong>4,000円</strong><small>(60分1件当り)平均36万円</small></div>
      <div class="pay-row"><span class="pay-tag part">パート</span>訪問単価 <strong>4,000円</strong><small>(60分1件当り)</small></div>
      <div class="pay-row"><span class="pay-tag part">パート</span>同行研修期間中 時給 <strong>2,000円</strong></div>
    </div>
    <dl class="terms">
      <dt>【資格】</dt><dd>各種職種に応じた資格</dd>
      <dt>【休日】</dt><dd>土・日・祝 年末年始休</dd>
      <dt>【時間】</dt><dd>正社員 9:00〜18:00<br>パート 1日3h、週1日からOK</dd>
      <dt>【待遇】</dt><dd>各種社会保険完備 賞与(業績に応じて)<br>交通費規定内支給</dd>
    </dl>
    <div class="org">
      <span class="org-mark"></span>
      <p class="org-name">みどり坂訪問看護リハビリステーション<small>緑ヶ丘市中央区本町1-2-3</small></p>
    </div>
  </section>

  <section class="col">
    <h2 class="col-title"><span class="dot">●</span>介護職員<br><span class="dot">●</span>登録ヘルパー <span class="dot">●</span>常勤ヘルパー</h2>
    <div class="pay">
      <div class="pay-row"><span class="pay-tag">正社員</span>月給 <strong>24万円〜</strong><small>(経験・資格により優遇)</small></div>
    </div>
    <div class="helper-grid">
      <span class="pay-tag part">身体介護</span><strong>2,000円〜</strong>
      <span class="pay-tag part">生活援助</span><strong>1,600円〜</strong>
      <span class="pay-tag">常勤</span><strong>1,400円〜</strong>
      <span class="pay-tag">移動支援</span><strong>1,200円〜</strong>
    </div>
    <dl class="terms">
      <dt>【資格】</dt><dd>各種職種に応じた資格</dd>
      <dt>【休日】</dt><dd>シフト制・希望休相談可</dd>
      <dt>【待遇】</dt><dd>社会保険完備 賞与(業績に応じて)<br>交通費規定内支給</dd>
    </dl>
    <div class="org">
      <p class="org-name">みどり坂訪問介護ステーション<small>緑ヶ丘市中央区本町1-2-3</small></p>
    </div>
  </section>
</main>

<footer>
  <div class="contact">
    <span class="label">応募先</span>
    <span class="phone">
      <svg width="36" height="36" viewBox="0 0 24 24" aria-hidden="true"><path fill="#2f8a2a" d="M6.6 10.8a15.1 15.1 0 0 0 6.6 6.6l2.2-2.2a1 1 0 0 1 1-.25 11.4 11.4 0 0 0 3.6.57 1 1 0 0 1 1 1V20a1 1 0 0 1-1 1A17 17 0 0 1 3 4a1 1 0 0 1 1-1h3.5a1 1 0 0 1 1 1c0 1.25.2 2.45.57 3.570a1 1 0 0 1-.25 1z"/></svg>
      012-345-6789
    </span>
    <span class="person">採用担当 / 佐藤 (有)ミドリケア</span>
  </div>
  <div class="footer-bar">土・日も安心! お気軽にお問い合わせください。</div>
</footer>
</body>
</html>
```